Anzeigengestaltung für Heilpraktikerin für Psychotherapie
Hallo lorvin, ich bin sehr zufrieden mit dem Design. Danke LG Karina Wehlert
Zielgruppe
Heilpraktikerin für Psychotherapie, Atem- und Körpertherapeutin, Einzelthearpie, Gruppentherapie, Menschen in Lebenskrisen; Menschen, die ihr Leben verändern wollen, Menschen suchen mehr Selbsterfahrung, vorwiegend Frauen, Atersgruppe 20 aufwärts, Menschen mit psychischen Problemen
Entspannung, Berühren, Massieren, Halten, Gespräch, Bewegen, Begleitung Während der Schwangerschaft, Geburt und danach, Trauerbegleitung
Aufgabenstellung
Name und Berufsbezeichnung sind mir wichtig
Praxiseröffnung, Termine nach Vereinbarung
aktuelles Angebot: Fantasiereise- Entspannung von Alltagsstress
sonstiges Angebot: Einzeltherapie/Gruppentherapie,

```html
<!DOCTYPE html>
<html lang="de">
<head>
<meta charset="utf-8">
<title>HerzOrt – Praxis-Neueröffnung</title>
<link rel="stylesheet" href="https://fonts.googleapis.com/css2?family=Open+Sans:ital,wght@0,400;0,600;0,700;1,400;1,700&display=swap">
<style>
  :root {
    --magenta: #e0268c;
    --magenta-soft: #ec7fb6;
    --plum: #5c2a5a;
    --plum-deep: #632c5c;
    --plum-text: #6d3b69;
    --sky-top: #dfe9f2;
    --sky-mid: #f3f6f9;
    --backdrop: #ebe8e4;
    --white: #ffffff;
  }
  * { margin: 0; padding: 0; box-sizing: border-box; }
  html, body { width: 1200px; height: 982px; overflow: hidden; }
  body {
    background: var(--backdrop);
    font-family: "Open Sans", Arial, sans-serif;
    position: relative;
  }
  .flyer {
    position: absolute;
    left: 38px; top: 78px;
    width: 1122px; height: 788px;
    overflow: hidden;
    background: linear-gradient(180deg, var(--sky-top) 0%, var(--sky-mid) 45%, #f7f5f3 75%, #e9e2dc 100%);
  }
  .photo-area {
    position: absolute; left: 0; top: 0;
    width: 560px; height: 788px;
    background: linear-gradient(90deg, #7a4a78 0%, #9a7aa0 30%, rgba(200,190,215,0.55) 65%, rgba(230,235,242,0) 100%);
  }
  .curves { position: absolute; left: 0; top: 0; }
  .web {
    position: absolute;
    left: 34px; top: 402px;
    transform: translate(-50%, -50%) rotate(-90deg);
    color: var(--white);
    font-weight: 700; font-size: 29px;
    white-space: nowrap;
  }
  .profession {
    position: absolute; left: 467px; top: 24px;
    font-size: 31px; color: var(--plum); font-weight: 400;
  }
  .headline-band {
    position: absolute; left: 297px; top: 87px;
    width: 825px; height: 87px;
    background: var(--magenta);
    color: var(--white);
    font-weight: 700; font-size: 57px; letter-spacing: 1px;
    line-height: 87px; padding-left: 12px;
  }
  .date {
    position: absolute; left: 445px; top: 190px;
    font-size: 50px; color: var(--plum);
  }
  .services {
    position: absolute; top: 276px;
    list-style: none;
    font-size: 23.5px; line-height: 37.8px; color: var(--plum);
  }
  .services li { position: relative; padding-left: 30px; }
  .services li::before {
    content: "◦"; position: absolute; left: 0; top: -1px;
    font-size: 22px;
  }
  .services li.cont::before { content: none; }
  .services.left { left: 452px; }
  .services.right { left: 726px; }
  .offer-badge {
    position: absolute; left: 122px; top: 180px;
    width: 280px; height: 280px; border-radius: 50%;
    background: var(--magenta);
    color: var(--white); text-align: center;
    font-style: italic; font-size: 23.5px; line-height: 31px;
    padding-top: 83px;
  }
  .offer-badge strong { font-weight: 700; display: block; }
  .appointment-badge {
    position: absolute; left: 85px; top: 492px;
    width: 170px; height: 170px; border-radius: 50%;
    background: var(--plum-deep);
    color: var(--white); text-align: center;
    font-style: italic; font-size: 22px; line-height: 27px;
    padding-top: 8px;
  }
  .appointment-badge strong { font-weight: 700; display: block; }
  .contact {
    position: absolute; left: 129px; top: 700px;
    color: var(--plum-text);
  }
  .contact .address { font-size: 28px; line-height: 36px; }
  .contact .email { font-size: 23px; line-height: 34px; }
  .brand {
    position: absolute; left: 690px; top: 560px;
    display: flex; align-items: center; gap: 18px;
    color: var(--plum);
  }
  .brand-dot { width: 34px; height: 34px; border-radius: 50%; background: var(--magenta); }
  .brand-name { font-size: 58px; font-weight: 600; }
</style>
</head>
<body>
  <main class="flyer">
    <div class="photo-area" role="img" aria-label="Foto: Frau im Meditationssitz vor Himmel und Meer"></div>

    <svg class="curves" width="1122" height="788" viewBox="0 0 1122 788" aria-hidden="true">
      <path d="M1040 0 C1080 120 1010 220 1000 340 C990 470 1070 560 1060 788" fill="none" stroke="#f2cfe0" stroke-width="18" opacity="0.7"/>
      <path d="M270 0 C210 110 190 200 240 310 C290 420 250 520 150 600 C90 650 55 720 45 788 L20 788 C30 700 70 630 130 580 C220 500 250 420 205 320 C160 210 180 100 235 0 Z" fill="var(--magenta-soft)" opacity="0.85"/>
      <path d="M240 0 C180 110 165 210 215 320 C260 420 225 510 130 590 C70 640 35 710 25 788 L0 788 L0 770 C15 690 55 620 115 570 C200 495 225 420 185 330 C140 220 150 100 205 0 Z" fill="var(--magenta)"/>
    </svg>

    <div class="web">www.herzort-praxis.org</div>

    <p class="profession">Heilpraktikerin für Psychotherapie</p>
    <h1 class="headline-band">PRAXIS-NEUERÖFFNUNG</h1>
    <p class="date">am 11.12.2017 in Altenried</p>

    <ul class="services left">
      <li>Einzeltherapie</li>
      <li>Gruppentherapie</li>
      <li>Frauengruppe</li>
      <li>Atemkaleingruppe</li>
      <li>Selbsterfahrung</li>
      <li>Jahreskreisgruppe</li>
    </ul>
    <ul class="services right">
      <li>offene Frauengruppe</li>
      <li>begleitete Atemsitzung</li>
      <li>unterstützende</li>
      <li>Begleitung während der</li>
      <li class="cont">Schwangerschaft, der Geburt</li>
      <li class="cont">und der Zeit danach</li>
    </ul>

    <div class="offer-badge">
      <strong>Aktuelles Angebot:</strong>
      Fantasiereise-<br>Entspannung von<br>Alltagsstress
    </div>

    <div class="appointment-badge">
      <strong>Termine<br>nach Ver-<br>einbarung</strong>
      0172 -<br>51 30 27 6
    </div>

    <address class="contact" style="font-style:normal">
      <div class="address">Lindenweg 14 • 72655 Altenried</div>
      <div class="email">herzort.karinawehlert@postfach-beispiel.de</div>
    </address>

    <div class="brand">
      <span class="brand-dot"></span>
      <span class="brand-name">HerzOrt</span>
    </div>
  </main>
</body>
</html>
```